We are in search of a new business card design for our business. We have a Mexican Grocery Store called Tortilla Grove Market, we would like to see that some have mexican design, but we are open to any type of designs.

Phone: to be announced
Fax: to be announced

Address is:
2415 Calloway Blvd
Harlow Point, MD 21907

```html
<!DOCTYPE html>
<html lang="en">
<head>
<meta charset="utf-8">
<title>Tortilla Grove Market – Business Card</title>
<link href="https://fonts.googleapis.com/css2?family=Lato:wght@400;700;900&display=swap" rel="stylesheet">
<style>
  :root {
    --backdrop: #1d1d1d;
    --card-white: #ffffff;
    --chili-red: #c8202a;
    --chili-deep: #8f1a22;
    --pepper-green: #2e8b3e;
    --text-light: #ffffff;
    --brand-red: #b81d26;
  }
  html, body {
    margin: 0;
    padding: 0;
    width: 1200px;
    height: 902px;
    overflow: hidden;
    background: var(--backdrop);
    font-family: "Lato", Arial, sans-serif;
  }
  .canvas {
    position: relative;
    width: 1200px;
    height: 902px;
  }
  .business-card {
    position: absolute;
    left: 100px;
    top: 166px;
    width: 1000px;
    height: 570px;
    border-radius: 22px;
    overflow: hidden;
    background: var(--card-white);
  }
  .card-shapes {
    position: absolute;
    inset: 0;
    width: 1000px;
    height: 570px;
  }
  .contact-panel {
    position: absolute;
    left: 48px;
    top: 74px;
    color: var(--text-light);
  }
  .employee-name {
    margin: 0;
    font-weight: 700;
    font-size: 33px;
    letter-spacing: 0.5px;
    line-height: 1.1;
  }
  .employee-role {
    margin: 0;
    font-weight: 400;
    font-size: 26px;
    line-height: 1.2;
  }
  .address {
    margin: 108px 0 0;
    font-style: normal;
    font-size: 26px;
    line-height: 34px;
  }
  .contact-list {
    list-style: none;
    margin: 48px 0 0;
    padding: 0;
    font-size: 26px;
    line-height: 32px;
  }
  .contact-list li {
    display: flex;
    align-items: center;
    gap: 12px;
  }
  .contact-icon {
    width: 30px;
    height: 22px;
    fill: var(--text-light);
    flex: none;
  }
  .brand-lockup {
    position: absolute;
    left: 560px;
    top: 0;
    width: 400px;
    height: 570px;
    display: flex;
    align-items: center;
    justify-content: center;
    gap: 16px;
  }
  .brand-dot {
    width: 34px;
    height: 34px;
    border-radius: 50%;
    background: var(--pepper-green);
    flex: none;
  }
  .brand-name {
    margin: 0;
    color: var(--brand-red);
    font-weight: 900;
    font-size: 46px;
    line-height: 1.05;
  }
</style>
</head>
<body>
<main class="canvas">
  <section class="business-card">
    <svg class="card-shapes" viewBox="0 0 1000 570" aria-hidden="true">
      <defs>
        <radialGradient id="panelGlow" cx="0.55" cy="0.5" r="0.75">
          <stop offset="0" stop-color="#d42328"/>
          <stop offset="1" stop-color="#93192a"/>
        </radialGradient>
      </defs>
      <path class="red-panel" d="M0 0 H506 Q368 285 506 570 H0 Z" fill="url(#panelGlow)"/>
      <path class="green-crescent" d="M514 0 Q368 285 514 570 L518 570 Q386 285 518 0 Z" fill="#2e8b3e"/>
    </svg>

    <div class="contact-panel">
      <h1 class="employee-name">EMPLOYEE NAME</h1>
      <p class="employee-role">Managing Director</p>
      <address class="address">2415 Calloway Blvd<br>Harlow Point, MD 21907</address>
      <ul class="contact-list">
        <li>
          <svg class="contact-icon" viewBox="0 0 30 22"><path d="M2 8 Q15 -2 28 8 L25 11 L21 8 L21 6 Q15 4 9 6 L9 8 L5 11 Z"/><path d="M8 10 H22 L26 20 H4 Z"/><circle cx="15" cy="15" r="3" fill="#b81d26"/></svg>
          <span>(01) 2345 6789</span>
        </li>
        <li>
          <svg class="contact-icon" viewBox="0 0 30 22"><rect x="8" y="1" width="14" height="6"/><rect x="2" y="8" width="26" height="9" rx="2"/><rect x="8" y="14" width="14" height="7" stroke="#b81d26" stroke-width="1.5"/></svg>
          <span>(01) 2345 6789</span>
        </li>
        <li>
          <svg class="contact-icon" viewBox="0 0 30 22"><rect x="2" y="2" width="26" height="18"/><path d="M2 2 L15 13 L28 2 M2 20 L12 11 M28 20 L18 11" stroke="#b81d26" stroke-width="1.6" fill="none"/></svg>
          <span>Info@yourcompany.com</span>
        </li>
      </ul>
    </div>

    <div class="brand-lockup">
      <span class="brand-dot"></span>
      <p class="brand-name">Tortilla Grove<br>Market</p>
    </div>
  </section>
</main>
</body>
</html>
```